Luxurious , elegant , fancy styling flat iron box

I need a flat iron box design for my new product . I’m interested in something fancy, elegant and sophisticated.
the name of the product is

Velvet Harbor

Elite World Class Performance
Nano Titanium Professional Flat Iron
Heats up to 470 degrees
Rated #1
Extention and Natural Hair Straighter for thick and course hair

Target Market(s)

Women

Industry/Entity Type

Hair And Beauty

Font styles to use
Script

Colors
1b1b1b
757575
5c5c5c

Requirements
Must have
• Fancy yet understandable writing
Should not have
• Too many colors , block writing

```html
<!DOCTYPE html>
<html lang="en">
<head>
<meta charset="utf-8">
<title>Velvet Harbor – Flat Iron Box</title>
<link href="https://fonts.googleapis.com/css2?family=Montserrat:ital,wght@0,300;0,400;0,500;0,600;1,600&display=swap" rel="stylesheet">
<style>
  :root{
    --stage:#e4e4e4;
    --box:#1b1b1b;
    --box-edge:#121212;
    --hair-dark:#2a2a2a;
    --hair-mid:#5c5c5c;
    --hair-light:#757575;
    --white:#f2f2f2;
    --soft:#d6d6d6;
    --gold:#d9a13b;
  }
  *{margin:0;padding:0;box-sizing:border-box}
  html,body{width:1200px;height:800px;overflow:hidden;background:var(--stage);font-family:"Montserrat",sans-serif}
  .dieline{position:relative;width:1200px;height:800px}
  .panel{position:absolute;background:var(--box);overflow:hidden;border:1px solid var(--box-edge)}
  .panel--top{left:300px;top:140px;width:860px;height:250px}
  .panel--front{left:300px;top:390px;width:860px;height:250px}
  .panel--end{left:50px;top:390px;width:250px;height:250px}

  .product-photo{position:absolute;top:10px;height:230px;border-radius:4px;
    background:
      linear-gradient(172deg, transparent 38%, rgba(10,10,10,.9) 40%, rgba(40,40,40,.9) 48%, transparent 50%),
      radial-gradient(ellipse at 40% 55%, var(--hair-light) 0%, var(--hair-mid) 28%, var(--hair-dark) 60%, var(--box) 85%);}
  .panel--front .product-photo{left:380px;right:12px}
  .panel--top .product-photo{left:380px;right:12px}

  .brand{position:absolute;color:var(--white);font-weight:300;letter-spacing:1px;white-space:nowrap}
  .title{position:absolute;left:34px;color:var(--soft);font-weight:500;font-size:22px;line-height:1.15;letter-spacing:.5px;text-transform:uppercase;white-space:nowrap}
  .heat{position:absolute;left:34px;color:var(--soft);font-weight:400;font-size:16px;letter-spacing:1px;text-transform:uppercase}
  .rating{position:absolute;color:var(--gold);font-weight:600;font-style:italic;font-size:17px}
  .tagline{position:absolute;right:26px;bottom:18px;color:var(--gold);font-weight:600;font-style:italic;font-size:11px;letter-spacing:.3px;white-space:nowrap}

  .panel--front .title{top:96px}
  .panel--front .heat{top:192px}
  .panel--front .brand{right:36px;top:22px;font-size:24px}
  .panel--front .rating{left:640px;top:70px}

  .panel--top .title{top:30px}
  .panel--top .heat{top:92px;font-size:13px}
  .panel--top .brand{left:34px;top:176px;font-size:28px}
  .panel--top .rating{left:620px;top:120px}

  .panel--end .brand{left:0;right:0;top:102px;text-align:center;font-size:30px}
</style>
</head>
<body>
<main class="dieline">
  <section class="panel panel--top">
    <div class="product-photo" role="img" aria-label="Black nano titanium flat iron resting over glossy straight dark hair"></div>
    <h2 class="title">Nano Titanium<br>Professional Flat Iron</h2>
    <p class="heat">Heats up to 470°</p>
    <p class="rating">Rated #1</p>
    <p class="tagline">Extention and Natural Hair Straighter for thick and course hair</p>
    <p class="brand">Velvet Harbor</p>
  </section>

  <section class="panel panel--end">
    <p class="brand">Velvet Harbor</p>
  </section>

  <section class="panel panel--front">
    <div class="product-photo" role="img" aria-label="Black nano titanium flat iron over flowing straight dark hair"></div>
    <h1 class="title">Nano Titanium<br>Professional Flat Iron</h1>
    <p class="heat">Heats up to 470°</p>
    <p class="brand">Velvet Harbor</p>
    <p class="rating">Rated #1</p>
    <p class="tagline">Extention and Natural Hair Straighter for thick and course hair</p>
  </section>
</main>
</body>
</html>
```